Business Card Design - Photographer

I am a landscape photographer and I require a business card design. 

I require two designs:
1)  a double sided business card
 and
b)  a single sided business card 

The single sided design can either be the same as the double sided (with just one side having all the information)....or it can be an entire new design. Its up to you.

My corporate colours are (CMYK):

Blue   69, 32, 0, 0
Grey  72,  64,  47,  31
Green  32,  2,  91,  0
Yellow   0, 19, 92, 0
Orange  0, 39, 75, 0

Colour space in final file should be in CMYK.

The details that need to be included on the card:

- Use the provided Logo
- Name: Wiktor Nowiradzki
- Email:   sales@framesbywiktor.com.au
- Website:    framesbywiktor.com.au
- Twitter:    twitter.com/framesbywiktor
- Facebook:   facebook.com/framesbywiktor
- Mobile  0419 356 782

Please use the attached template to design the logo to the specified size, including the marked bleed lines. I have also attached my logo in PNG (transparent background) and ai format for you to use.

The final file should be:
- Photoshop version with layers so I can edit the name/text etc. All non vector files should be high resolution at 1039 x 697 pixels at 300 dpi.

I also require a file as:
- Vector based PDF

Anyway questions please contact me.

Thank you

Industry/Entity Type

Landscape

Logo styles of interest
Pictorial/Combination Logo
Abstract Logo
Wordmark Logo
Lettermark Logo
Requirements
Must have
• The details that need to be included on the card:

- Use the provided Logo
- Name: Wiktor Nowiradzki
- Email: sales@framesbywiktor.com.au
- Website: framesbywiktor.com.au
- Twitter: twitter.com/framesbywiktor
- Facebook: facebook.com/framesbywiktor
- Mobile 0419 356 782

```html
<!DOCTYPE html>
<html lang="en">
<head>
<meta charset="utf-8">
<title>Frames by Wiktor – Business Card</title>
<link href="https://fonts.googleapis.com/css2?family=Cabin:wght@400;600&display=swap" rel="stylesheet">
<style>
  :root {
    --stage: #2b201c;
    --card-dark: #050505;
    --card-light: #f4f3f1;
    --ink: #3e3e3e;
    --ink-soft: #555555;
    --orange: #e8741c;
    --orange-line: #f2a43a;
    --mark-grey: #a9a9a9;
    --brand-circle: #3b3f4a;
  }
  * { margin: 0; padding: 0; box-sizing: border-box; }
  html, body { width: 1200px; height: 800px; overflow: hidden; }
  body {
    background: var(--stage);
    font-family: "Cabin", sans-serif;
    position: relative;
  }
  .card {
    position: absolute;
    top: 246px;
    width: 540px;
    height: 309px;
    overflow: hidden;
  }
  /* Front */
  .card--front { left: 45px; background: var(--card-dark); }
  .front__leaves {
    position: absolute;
    left: 0; top: 16px;
    width: 175px; height: 293px;
    background: radial-gradient(ellipse at 40% 50%, #1a1a1a 0%, #111 55%, rgba(5,5,5,0) 80%);
  }
  .front__name {
    position: absolute;
    left: 0; right: 0; top: 143px;
    text-align: center;
    color: var(--orange);
    font-weight: 600;
    font-size: 16px;
  }
  /* Back */
  .card--back { left: 615px; background: var(--card-light); color: var(--ink); }
  .crop-marks { position: absolute; inset: 0; }
  .brand {
    position: absolute;
    left: 0; right: 0; top: 66px;
    text-align: center;
  }
  .brand__circle {
    width: 62px; height: 62px;
    border-radius: 50%;
    background: var(--brand-circle);
    margin: 0 auto 14px;
  }
  .brand__name {
    font-size: 18px;
    font-weight: 400;
    letter-spacing: 1.5px;
    color: #222;
  }
  .back__name {
    position: absolute;
    left: 0; right: 0; top: 190px;
    text-align: center;
    font-weight: 600;
    font-size: 14px;
    color: var(--ink);
  }
  .contacts {
    position: absolute;
    top: 232px;
    font-size: 11.5px;
    color: var(--ink-soft);
    line-height: 17.5px;
    list-style: none;
  }
  .contacts--left { left: 108px; }
  .contacts--right { left: 322px; }
  .contacts li { display: flex; align-items: center; gap: 6px; }
  .contacts svg { flex: none; }
  .social-square { width: 12px; height: 12px; background: #3a3a3a; flex: none; }
  .website {
    position: absolute;
    left: 0; right: 0; top: 273px;
    display: flex; align-items: center; gap: 6px;
  }
  .website__rule { flex: 1; height: 1.5px; background: var(--orange-line); }
  .website__url { color: var(--orange-line); font-size: 13px; }
</style>
</head>
<body>
  <section class="card card--front">
    <div class="front__leaves" role="img" aria-label="Faint dark leaf spray decoration along the left edge"></div>
    <p class="front__name">Wiktor Nowiradzki</p>
  </section>

  <section class="card card--back">
    <svg class="crop-marks" width="540" height="309" viewBox="0 0 540 309" fill="none" stroke="var(--mark-grey)" stroke-width="2.5">
      <path d="M65 49 V37 H77"/>
      <path d="M463 37 H475 V49"/>
      <path d="M65 182 V194 H77"/>
      <path d="M463 194 H475 V182"/>
    </svg>

    <div class="brand">
      <div class="brand__circle"></div>
      <p class="brand__name">FRAMES BY WIKTOR</p>
    </div>

    <p class="back__name">Wiktor Nowiradzki</p>

    <ul class="contacts contacts--left">
      <li>
        <svg width="10" height="13" viewBox="0 0 10 13"><rect x="1.5" y="0.75" width="7" height="11.5" rx="1.2" fill="none" stroke="#3a3a3a" stroke-width="1.3"/><line x1="4" y1="10.2" x2="6" y2="10.2" stroke="#3a3a3a" stroke-width="1.2"/></svg>
        0419 356 782
      </li>
      <li>
        <svg width="12" height="9" viewBox="0 0 12 9"><rect x="0.5" y="0.5" width="11" height="8" fill="#3a3a3a"/><path d="M0.8 0.8 L6 5 L11.2 0.8" fill="none" stroke="#f4f3f1" stroke-width="1"/></svg>
        sales@framesbywiktor.com.au
      </li>
    </ul>

    <ul class="contacts contacts--right">
      <li><span class="social-square"></span>framesbywiktor</li>
      <li><span class="social-square"></span>framesbywiktor</li>
    </ul>

    <div class="website">
      <span class="website__rule"></span>
      <span class="website__url">www.framesbywiktor.com.au</span>
      <span class="website__rule"></span>
    </div>
  </section>
</body>
</html>
```